Web site design for BrixaForm Software (www.brixaformsoftware.example)

Need the design as well as the html for the website. The brief is given in the attached file.
If possible, would like to use pencil sketches instead of images to give a unique look to the site.
Target Market(s)
small Software product companies
Industry/Entity Type
Software
Coding
Coded - Design and coding required
Number of Pages Required
5+ page

```html
<!DOCTYPE html>
<html lang="en">
<head>
<meta charset="utf-8">
<title>BrixaForm Software</title>
<link href="https://fonts.googleapis.com/css2?family=Comfortaa:wght@400;700&family=Courier+Prime:wght@400;700&display=swap" rel="stylesheet">
<style>
:root{
  --cream:#f4ebc6;
  --cream-light:#f7f0d3;
  --cream-band:#f2e8bf;
  --brown:#3e2a17;
  --brown-line:#5a4129;
  --orange:#cf560f;
  --grey-title:#666158;
  --ink:#2a2018;
  --btn-grey:#6b6a66;
}
*{box-sizing:border-box;margin:0;padding:0}
html,body{width:1200px;height:3774px;overflow:hidden}
body{background:var(--cream);font-family:"Courier Prime","Courier New",monospace;color:var(--ink);position:relative}
a{color:inherit;text-decoration:none}
.section{position:absolute;left:0;width:1200px}
.wrap{position:relative;width:822px;margin:0 auto}

/* header */
.site-header{top:0;height:175px;background:var(--cream)}
.brand{position:absolute;left:189px;top:22px;font-family:"Comfortaa",sans-serif;font-weight:700;font-size:56px;color:var(--ink);letter-spacing:-1px}
.social{position:absolute;right:190px;top:34px;display:flex;gap:10px}
.social span{width:40px;height:40px;border-radius:50%;background:var(--ink);display:block}
.main-nav{position:absolute;left:189px;top:122px;width:822px;display:flex;gap:24px;font-size:15px;border-bottom:1px solid #d8cda4;padding-bottom:12px}
.main-nav a.current{color:var(--orange)}
.main-nav .more{margin-left:auto}

/* hero */
.hero{top:175px;height:990px}
.hero-title{position:absolute;left:0;width:1200px;text-align:center;font-weight:700;line-height:1}
.hero-title .line1{display:block;font-size:72px;color:var(--grey-title);margin-top:24px;text-shadow:2px 2px 0 #c8bfa0}
.hero-title .line2{display:block;font-size:72px;color:var(--orange);margin-top:-6px;text-shadow:2px 2px 0 #9b8f6a}
.btn{display:inline-block;background:var(--orange);color:#fff;font-size:13px;padding:6px 16px;border-radius:6px}
.btn.grey{background:var(--btn-grey)}
.hero .btn{position:absolute;left:541px;top:153px}
.sketch{position:absolute;left:189px;top:200px;width:822px;height:292px;background:linear-gradient(180deg,#f3efe4 0%,#bcb7aa 55%,#8a867c 100%)}
.quote{position:absolute;left:189px;top:492px;width:822px;height:188px;background:var(--brown);color:#fff;text-align:center;padding-top:46px}
.quote p{font-family:"Comfortaa",sans-serif;font-size:17px;line-height:1.6;width:700px;margin:0 auto}
.quote cite{display:block;font-style:normal;color:var(--orange);font-size:13px;margin-top:12px}
.intro{position:absolute;left:300px;top:705px;width:600px;text-align:center;font-weight:700;font-size:14.5px;line-height:30px}
.hero .intro-btn{left:541px;top:912px}

/* section titles */
.section-title{text-align:center;font-weight:700;font-size:40px;color:var(--grey-title);text-shadow:2px 2px 0 #cfc6a6}

/* services */
.services{top:1165px;height:546px;background:var(--cream-light)}
.services .section-title{position:absolute;top:60px;width:1200px}
.service-grid{position:absolute;left:189px;top:123px;width:822px;display:grid;grid-template-columns:repeat(3,1fr);gap:6px}
.service{background:var(--brown);color:#fff;height:174px;text-align:center;padding:18px 22px}
.service h3{font-size:19px;font-weight:700;line-height:1.05}
.service p{font-size:13px;line-height:1.3;margin-top:8px}
.service .more-link{display:block;color:var(--orange);font-size:12px;margin-top:14px}
.service.all{background:var(--orange);display:flex;align-items:center;justify-content:center;font-size:24px;font-weight:700;line-height:1.2}

/* about */
.about{top:1711px;height:382px;background:var(--cream)}
.about .section-title{position:absolute;top:60px;width:1200px}
.about-text{position:absolute;left:250px;top:115px;width:700px;text-align:center;font-weight:700;font-size:14.5px;line-height:33px}
.about .btn{position:absolute;left:541px;top:287px}

/* engagement */
.engagement{top:2093px;height:541px;background:var(--brown);color:#fff}
.engagement .section-title{position:absolute;top:60px;width:1200px;color:var(--orange);text-shadow:2px 2px 0 #1f140a}
.models{position:absolute;left:230px;top:150px;width:740px;height:350px;display:grid;grid-template-columns:1fr 1fr;grid-template-rows:1fr 1fr}
.model{text-align:center;padding:0 22px}
.model:nth-child(1),.model:nth-child(2){border-bottom:1px solid var(--brown-line)}
.model:nth-child(1),.model:nth-child(3){border-right:1px solid var(--brown-line)}
.model:nth-child(3),.model:nth-child(4){padding-top:18px}
.model h3{color:var(--orange);font-size:19px;font-weight:700;line-height:1.1}
.model p{font-size:13.5px;line-height:1.35;margin-top:8px}

/* work with us */
.work{top:2634px;height:556px;background:var(--cream)}
.work .section-title{position:absolute;top:60px;width:1200px}
.work-body{position:absolute;left:189px;top:126px;width:822px;font-size:13.5px;line-height:1.3}
.clipping{float:left;width:328px;height:172px;margin:0 22px 4px 0;background:linear-gradient(135deg,#d8c79a 0%,#b59d6a 60%,#8f7a50 100%)}
.work .btn{position:absolute;left:189px;top:463px}

/* partners */
.partners{top:3190px;height:295px;background:var(--cream-light)}
.partners .section-title{position:absolute;top:60px;width:1200px}
.badges{position:absolute;left:189px;top:135px;width:822px;display:flex;justify-content:space-between}
.badge{width:82px;height:82px;border-radius:50%;border:3px solid #4a4540;background:#efe8d3}
.badge.solid{background:#3a3631}

/* footer */
.site-footer{top:3485px;height:289px;background:var(--cream)}
.footer-nav{position:absolute;left:0;width:1200px;top:66px;text-align:center;font-size:15px;line-height:30px}
.footer-nav a{margin:0 9px}
.footer-nav a.current{color:var(--orange)}
.site-footer .social{position:absolute;left:521px;right:auto;top:163px}
.copyright{position:absolute;left:0;width:1200px;top:248px;text-align:center;font-size:11px;color:#7b705c}
</style>
</head>
<body>

<header class="section site-header">
  <div class="brand">BrixaForm</div>
  <div class="social" aria-label="Social links"><span></span><span></span><span></span><span></span></div>
  <nav class="main-nav">
    <a class="current" href="#">Home</a><a href="#">Services</a><a href="#">About Us</a><a href="#">Expertise</a><a href="#">Engagement Models</a><a href="#">Agile</a><a href="#">Case studies</a><a class="more" href="#">More ▾</a>
  </nav>
</header>

<section class="section hero">
  <h1 class="hero-title"><span class="line1">All About</span><span class="line2">Engineering</span></h1>
  <a class="btn grey" href="#">Learn More</a>
  <div class="sketch" role="img" aria-label="Pencil sketch of a suspension bridge spanning a wooded gorge"></div>
  <blockquote class="quote">
    <p>"Perfection is achieved not when there is nothing more to add, but when there is nothing left to take away."</p>
    <cite>-Aurel Vasquez</cite>
  </blockquote>
  <p class="intro">Design pervades nature. Whether it is the unique symmetry of a snowflake, or the fibonnacci number of a sunflower or nautilus shell, or self replicating fractals, design is everywhere.<br>In todays world, Good Design is associated more with tangible products, and User interfaces. But good design has always been part of software engineering. Good design is what enables massive software edifices to remain stable.</p>
  <a class="btn intro-btn" href="#">Learn More</a>
</section>

<section class="section services">
  <h2 class="section-title">Services</h2>
  <div class="service-grid">
    <div class="service"><h3>POC</h3><p>Whether it is a mobile or web app prototype, or a more complex IOTprototype, our engineers can...</p><a class="more-link" href="#">View More</a></div>
    <div class="service"><h3>BUILD PRODUCT</h3><p>Our team of analysts, design thinkers and technologists work with client and end users to specify...</p><a class="more-link" href="#">View More</a></div>
    <div class="service"><h3>MAINTAIN PRODUCT</h3><p>We have the ability to quickly understand large, legacy products, write scaffold test...</p><a class="more-link" href="#">View More</a></div>
    <div class="service"><h3>ODC SETUP</h3><p>We help in setting up Offshore Development centres for small and medium software development...</p><a class="more-link" href="#">View More</a></div>
    <div class="service"><h3>ARCHITECTURAL INTERVENTIONS</h3><p>Does your product refuse to scale? Is it hogged down by unpredictable...</p><a class="more-link" href="#">View More</a></div>
    <a class="service all" href="#">View All<br>Services</a>
  </div>
</section>

<section class="section about">
  <h2 class="section-title">About Us</h2>
  <p class="about-text">We are seasoned programmers, interested in the science as well as the craft of programming.<br><span style="display:block;height:14px"></span>We need to put high res black and white photos of Arvind - followed by a paragraph about Arvind</p>
  <a class="btn" href="#">Learn More</a>
</section>

<section class="section engagement">
  <h2 class="section-title">Engagement Models</h2>
  <div class="models">
    <div class="model"><h3>OPD</h3><p>We provide pure Outsourced product development for either new software development or product maintenance. Agile contracts and deliverable based compensation ensure value for customer and end users.</p></div>
    <div class="model"><h3>EQUITY BASED</h3><p>If you are a startup with very strong growth potential, we are interested. We can work out a equity-compensation mix that can help you get to market faster with a lower burn rate.</p></div>
    <div class="model"><h3>BOT</h3><p>We help in setting up a team in India, gather expertise in your product and domain, grow the team and finally spin it off as your captive subsidiary/</p></div>
    <div class="model"><h3>ARCHITECTURAL AND PROCESS CONSULTANCY</h3><p>Kavi/Arvind could you please add some meat here?</p></div>
  </div>
</section>

<section class="section work">
  <h2 class="section-title">Work With Us</h2>
  <div class="work-body">
    <div class="clipping" role="img" aria-label="Old newspaper clipping of a men wanted advertisement"></div>
    <p>BrixaForm works with small and midsize product development companies. It uses design thinking and rigourous software development principles to build world class products<br>
    Working in BrixaForm requires very strong grounding in computer science, ability to put in hours of concentrated work, and continuous learning. Every programmer is also a tester, a business analyst, a communicator, and sometimes a good UI programmer too!<br>
    We require people who realise the importance of extremely good communication skills (listening being the most important), a desire to keep on learning, collaborate with others, and humility over all else.<br>
    You will get opportunities for learning more and more - not always newer technologies, because sometimes the older ways are better. You get to work with people with over 3 decades of programming experience. You get to work with the best in technologies, time and backing to explore new technologies.</p>
  </div>
  <a class="btn" href="#">Learn More</a>
</section>

<section class="section partners">
  <h2 class="section-title">Partners</h2>
  <div class="badges" aria-label="Partner badges">
    <span class="badge"></span><span class="badge"></span><span class="badge solid"></span><span class="badge"></span><span class="badge solid"></span><span class="badge"></span>
  </div>
</section>

<footer class="section site-footer">
  <nav class="footer-nav">
    <a class="current" href="#">Home</a><a href="#">Services</a><a href="#">About Us</a><a href="#">Expertise</a><a href="#">Engagement Models</a><a href="#">Agile</a><a href="#">Case studies</a><br>
    <a href="#">Work with us</a><a href="#">Accolades</a><a href="#">Stories</a><a href="#">Partners</a><a href="#">Giving back</a><a href="#">blog</a><a href="#">Contact Us</a>
  </nav>
  <div class="social" aria-label="Social links"><span></span><span></span><span></span><span></span></div>
  <p class="copyright">©2017 BrixaForm. All rights reserved.</p>
</footer>

</body>
</html>
```